Business Card Design Project

Hello! We need a business card design for a new company opening up in Downtown Dallas called Marbrook Cupcakes. We are a cupcake factory and our primary colors are Harbor Teal and Brown. We want to have a design that can be used for multiple positions (Owner/Operations Manager, Assistant Operations Manager, Decorator, Baker, Corporate Sale Rep, Special Events Rep etc) We would like for it to be double sided. Use the following information in your designs:

Renata Vasquill
Assistant Operations Manager
renata@marbrookcupcakes.example
T555.318.9047

Store Hours:
Mon-Thur 10am-9pm
Fri-Sat 10am-10pm
Sun 12pm-7pm

website: www.marbrookcupcakes.example

Address: 2735 Quarry Ln, Dallas TX 75999

The logo is attached.

Industry/Entity Type

Business

Requirements
Must have
• It must be Harbor Teal and Brown.
Nice to have
• Nice for it to be double sided.
Should not have
• No graphics like a cupcake. Just the word logo.

```html
<!DOCTYPE html>
<html lang="en">
<head>
<meta charset="utf-8">
<title>Marbrook Cupcakes – Business Card</title>
<link rel="stylesheet" href="https://fonts.googleapis.com/css2?family=Mulish:wght@400;600&display=swap">
<style>
  :root {
    --harbor-teal: #5cbcc2;
    --teal-deep: #3f9ea5;
    --cocoa: #4a2a22;
    --ink: #3a3330;
    --paper: #fbfbfa;
    --backdrop: #e7e9e8;
  }
  * { box-sizing: border-box; margin: 0; padding: 0; }
  html, body {
    width: 1200px; height: 900px; overflow: hidden;
    background: var(--backdrop);
    font-family: "Mulish", sans-serif;
  }
  .sheet {
    width: 1200px; height: 900px;
    display: flex; flex-direction: column;
    align-items: center; justify-content: center; gap: 36px;
  }
  .card {
    position: relative;
    width: 700px; height: 400px;
    box-shadow: 0 8px 24px rgba(0,0,0,.18);
    overflow: hidden;
  }

  /* Front side */
  .card--front { background: var(--paper); }
  .wordmark {
    position: absolute; top: 58px; right: 52px;
    font-size: 40px; font-weight: 600; letter-spacing: .02em;
    color: var(--harbor-teal);
  }
  .holder {
    position: absolute; left: 44px; top: 210px; width: 610px;
  }
  .holder__name {
    font-size: 27px; font-weight: 400; letter-spacing: .12em;
    color: var(--harbor-teal);
  }
  .holder__title {
    margin-top: 4px;
    font-size: 14px; letter-spacing: .1em; color: var(--cocoa);
  }
  .holder__rule {
    margin-top: 12px; width: 360px; height: 1px;
    background: linear-gradient(90deg, var(--cocoa), rgba(74,42,34,0));
  }
  .contact {
    margin-top: 22px;
    font-size: 15px; line-height: 1.75; letter-spacing: .06em;
    color: var(--ink);
  }
  .band-rule {
    position: absolute; left: 0; right: 0; bottom: 30px; height: 2px;
    background: var(--cocoa);
  }
  .band {
    position: absolute; left: 0; right: 0; bottom: 0; height: 30px;
    background: var(--teal-deep);
  }

  /* Back side */
  .card--back {
    background: linear-gradient(135deg, var(--harbor-teal), #7fcfd3 60%, var(--harbor-teal));
  }
  .back-mark {
    position: absolute; left: 0; right: 0; top: 120px;
    display: flex; align-items: center; justify-content: center; gap: 22px;
  }
  .back-mark__dot {
    width: 64px; height: 64px; border-radius: 50%;
    border: 3px solid rgba(255,255,255,.9);
  }
  .back-mark__name {
    font-size: 52px; font-weight: 600; letter-spacing: .02em;
    color: #ffffff;
  }
  .hours {
    position: absolute; right: 44px; bottom: 40px;
    font-size: 15px; line-height: 1.6; letter-spacing: .05em;
    color: var(--cocoa); text-align: right;
  }
</style>
</head>
<body>
<main class="sheet">
  <section class="card card--front" aria-label="Card front">
    <div class="wordmark">Marbrook Cupcakes</div>
    <div class="holder">
      <h1 class="holder__name">Renata Vasquill</h1>
      <p class="holder__title">Assistant Operations Manager</p>
      <div class="holder__rule"></div>
      <p class="contact">
        2735 Quarry Ln, Dallas TX 75999 | T: 555.318.9047<br>
        E: renata@marbrookcupcakes.example | www.marbrookcupcakes.example
      </p>
    </div>
    <div class="band-rule"></div>
    <div class="band"></div>
  </section>

  <section class="card card--back" aria-label="Card back">
    <div class="back-mark">
      <span class="back-mark__dot"></span>
      <span class="back-mark__name">Marbrook Cupcakes</span>
    </div>
    <p class="hours">
      Store Hours: Mon-Thur 10am-9pm<br>
      Fri-Sat 10am-10pm • Sun 12pm-7pm
    </p>
  </section>
</main>
</body>
</html>
```